依頼詳細
お客様にわかりやすく、またチラシをみてポイントカードを持っておきたい、もらっておきたいと思わせるデザインを希望します。お客様の目に入りやすく、A1のポスターや、レジ横でA4の用紙に置く予定です。
内容はジュース1杯で1P
10Pでお好きなドリンク1杯サービスです!(どのサイズでも)
入会費、年会費無料、有効期限なし!
記載項目
ポイントカード
サイズ
A4
ページ数
片面
希望イメージ
シンプル 複雑
単色 カラフル
暗い 明るい
日常 高級
遊び心 厳粛
未来的 伝統的
女性的 男性的
希望する色
黄・オレンジ系
納品ファイル
• 高解像度JPG (.jpg)
補足説明
参考イメージ添付します。
依頼公開後の追記内容
ポイントカード画像を添付します。
■ 選んだ理由

ポイントカードが目立つ

■ 提案者全員のお礼・コメント

どれもレベルが高い提案で選ぶことが難しかったです。また機会がございましたらよろしくお願いします。

```html
<!DOCTYPE html>
<html lang="ja">
<head>
<meta charset="utf-8">
<title>ポイントカード会員募集中</title>
<link href="https://fonts.googleapis.com/css2?family=M+PLUS+Rounded+1c:wght@700;800;900&family=Dela+Gothic+One&family=Pacifico&display=swap" rel="stylesheet">
<style>
  :root{
    --orange:#f7941d;
    --orange-deep:#f07d12;
    --orange-light:#fbb040;
    --yellow:#ffe13a;
    --red:#e8392b;
    --white:#ffffff;
    --ink:#3a2a1c;
    --cream:#fff6e3;
  }
  *{margin:0;padding:0;box-sizing:border-box}
  html,body{width:849px;height:1200px;overflow:hidden}
  body{font-family:"M PLUS Rounded 1c",sans-serif;color:var(--ink)}
  .poster{
    position:relative;width:849px;height:1200px;overflow:hidden;
    background:radial-gradient(circle at 50% 40%,var(--orange-light) 0%,var(--orange) 55%,var(--orange-deep) 100%);
  }
  .deal-tag{
    position:absolute;left:26px;top:40px;padding:10px 26px;
    background:var(--red);color:var(--white);font-weight:900;font-size:36px;
    transform:rotate(-10deg);border-radius:6px;
  }
  .tagline{
    position:absolute;left:0;right:0;top:72px;text-align:center;
    color:var(--red);font-weight:900;font-size:40px;letter-spacing:2px;
  }
  .tagline::before,.tagline::after{content:"";display:inline-block;width:4px;height:40px;background:var(--red);vertical-align:middle;margin:0 22px;border-radius:2px}
  .tagline::before{transform:rotate(-30deg)}
  .tagline::after{transform:rotate(30deg)}
  .script-mark{
    position:absolute;right:110px;top:52px;font-family:"Pacifico",cursive;
    color:rgba(255,255,255,.75);font-size:34px;transform:rotate(-8deg);
  }
  .headline{
    position:absolute;left:0;right:0;top:150px;text-align:center;
    font-family:"Dela Gothic One",sans-serif;font-size:104px;color:var(--white);
    -webkit-text-stroke:10px var(--red);paint-order:stroke fill;letter-spacing:2px;
  }
  .recruit{
    position:absolute;left:50%;top:290px;transform:translateX(-50%);
    background:var(--red);color:var(--white);border-radius:60px;
    padding:4px 46px;font-family:"Dela Gothic One",sans-serif;font-size:70px;letter-spacing:8px;
    white-space:nowrap;
  }
  .panel{
    position:absolute;left:62px;top:340px;width:725px;height:740px;
    background:var(--white);border-radius:28px;
  }
  .cards{position:absolute;left:0;top:0;width:849px;height:1200px}
  .rule-small{
    position:absolute;left:490px;top:430px;font-weight:800;font-size:34px;letter-spacing:2px;
  }
  .rule-small b{color:var(--red);font-size:44px;font-weight:900}
  .goal{
    position:absolute;left:0;right:0;top:730px;text-align:center;font-weight:900;font-size:46px;
  }
  .goal .badge{
    display:inline-block;background:var(--orange-light);color:var(--ink);
    border-radius:50%;padding:16px 20px;font-size:52px;line-height:1;margin-right:4px;
  }
  .reward{
    position:absolute;left:0;right:0;top:820px;text-align:center;font-weight:900;
    font-size:58px;line-height:1.25;letter-spacing:3px;
  }
  .any-size{
    position:absolute;left:50%;top:985px;transform:translateX(-50%);white-space:nowrap;
    background:var(--yellow);border-radius:40px;padding:6px 38px;font-weight:900;font-size:32px;
  }
  .cup{
    position:absolute;top:760px;width:180px;height:330px;border-radius:10px 10px 40px 40px;
    background:linear-gradient(180deg,rgba(255,255,255,.6) 0%,var(--yellow) 30%,var(--orange-light) 100%);
  }
  .cup.left{left:-20px}
  .cup.right{right:-20px}
  .perks{position:absolute;left:30px;right:30px;top:1072px;display:flex;gap:22px}
  .perk{flex:1;background:var(--white);border-radius:12px;overflow:hidden;text-align:center;height:116px}
  .perk-label{background:var(--red);color:var(--white);font-weight:800;font-size:26px;padding:4px 0}
  .perk-value{color:var(--red);font-family:"Dela Gothic One",sans-serif;font-size:56px;line-height:76px}
</style>
</head>
<body>
<div class="poster">
  <div class="deal-tag">おトクな</div>
  <div class="tagline">どんどん飲もう！</div>
  <div class="script-mark">point card</div>
  <div class="headline">ポイントカード</div>
  <div class="panel"></div>
  <div class="recruit">会員募集中！</div>

  <svg class="cards" viewBox="0 0 849 1200" role="img" aria-label="ポイントカードのイラスト：1個押したカードから10個たまったカードへ">
    <rect x="250" y="440" width="190" height="110" rx="8" fill="#f7941d"/>
    <g fill="#fff6e3">
      <rect x="262" y="475" width="30" height="28" rx="3"/><rect x="297" y="475" width="30" height="28" rx="3"/><rect x="332" y="475" width="30" height="28" rx="3"/><rect x="367" y="475" width="30" height="28" rx="3"/><rect x="402" y="475" width="30" height="28" rx="3"/>
      <rect x="262" y="508" width="30" height="28" rx="3"/><rect x="297" y="508" width="30" height="28" rx="3"/><rect x="332" y="508" width="30" height="28" rx="3"/><rect x="367" y="508" width="30" height="28" rx="3"/><rect x="402" y="508" width="30" height="28" rx="3"/>
    </g>
    <path d="M255 560 Q255 640 320 640" fill="none" stroke="#e8392b" stroke-width="14" stroke-linecap="round"/>
    <path d="M312 615 L345 640 L312 665 Z" fill="#e8392b"/>
    <rect x="345" y="545" width="350" height="175" rx="10" fill="#f7941d"/>
    <g fill="#fff6e3">
      <rect x="362" y="595" width="56" height="52" rx="4"/><rect x="427" y="595" width="56" height="52" rx="4"/><rect x="492" y="595" width="56" height="52" rx="4"/><rect x="557" y="595" width="56" height="52" rx="4"/><rect x="622" y="595" width="56" height="52" rx="4"/>
      <rect x="362" y="655" width="56" height="52" rx="4"/><rect x="427" y="655" width="56" height="52" rx="4"/><rect x="492" y="655" width="56" height="52" rx="4"/><rect x="557" y="655" width="56" height="52" rx="4"/><rect x="622" y="655" width="56" height="52" rx="4"/>
    </g>
  </svg>

  <div class="rule-small">ジュース<b>1</b>杯で <b>1P</b></div>

  <div class="cup left" role="img" aria-label="オレンジジュースのカップのイラスト"></div>
  <div class="cup right" role="img" aria-label="オレンジジュースのカップのイラスト"></div>

  <div class="goal"><span class="badge">10P</span>で</div>
  <div class="reward">お好きなドリンク<br>1杯サービス！</div>
  <div class="any-size">どのサイズでもOK！</div>

  <div class="perks">
    <div class="perk"><div class="perk-label">入会費</div><div class="perk-value">無料</div></div>
    <div class="perk"><div class="perk-label">年会費</div><div class="perk-value">無料</div></div>
    <div class="perk"><div class="perk-label">有効期限</div><div class="perk-value">なし</div></div>
  </div>
</div>
</body>
</html>
```